Drifting Marlo’s Coffee + Cannabis Packaging Design

Drifting Marlo's Coffee + Cannabis is a coffee shop dispensary in Albuquerque New Mexico. We need a packaging design for two bag sizes. 4'x5" and 3.4"x4". Our slogan is "Roasted + Toasted". We’re opening this year (2023) so a new company. Essentially I’d like the design to have the look of a National brand even though we’re a local New Mexico company. I don’t want anything super modern looking. There’s a back story you can find and read at www.driftingmarlosnm-example.com.

I’ve attached examples
Updates

A thought also that I really like, these will be 1g and 3.5G bags for cannabis. I like the idea of making them look like little coffee bags…

Target Market(s)

Persons 21-65

Industry/Entity Type

Cannabis + Coffee

Font styles to use
Other font styles liked:
• High Voltage Rough preferred but if the design is right I’d deviate

Colors

Designer to choose colors to be used in the design.

Requirements
Must have
• Drifting Marlo’s names a must. doesn’t have to have the logo. Just the same font.
Should not have
• Cartoon feels

```html
<!DOCTYPE html>
<html lang="en">
<head>
<meta charset="UTF-8">
<title>Drifting Marlo’s Coffee + Cannabis — Pouch Designs</title>
<link href="https://fonts.googleapis.com/css2?family=Fjalla+One&family=Oswald:wght@500&family=Arimo:wght@400;700&display=swap" rel="stylesheet">
<style>
  :root {
    --stage: #8c8c8c;
    --bag-dark: #0d0d0d;
    --bag-light: #eeeeec;
    --gold: #c9a04f;
    --gold-light: #ecd592;
    --gold-deep: #9a7530;
    --brown: #5a3e2b;
    --brown-band: #5b3d2b;
    --tan: #b58352;
    --white: #f4f4f4;
    --leaf: #5f8444;
    --leaf-light: #8fae6f;
    --bean: #4e301c;
    --bean-light: #8a5a37;
    --warn-red: #c62828;
  }
  * { box-sizing: border-box; margin: 0; padding: 0; }
  html, body { width: 1200px; height: 800px; overflow: hidden; }
  body { background: var(--stage); position: relative; font-family: "Arimo", sans-serif; }

  .pouch {
    position: absolute; top: 82px; width: 410px; height: 661px;
    border-radius: 22px; overflow: hidden;
  }
  .pouch--dark { left: 157px; background: var(--bag-dark); }
  .pouch--light { left: 626px; background: var(--bag-light); }

  .pouch__art { position: absolute; left: 0; top: 0; width: 410px; height: 661px; }

  .pouch__mark {
    position: absolute; left: 50%; top: 164px; width: 34px; height: 34px;
    margin-left: -17px; border-radius: 50%; background: var(--gold);
  }
  .pouch--light .pouch__mark { background: var(--tan); }

  .pouch__name {
    position: absolute; left: 0; top: 236px; width: 100%; text-align: center;
    font-family: "Fjalla One", sans-serif; font-weight: 400; font-size: 38px; line-height: 1;
    color: var(--white);
  }
  .pouch--light .pouch__name { color: var(--brown); }

  .pouch__tagline {
    position: absolute; left: 0; top: 283px; width: 100%; text-align: center;
    font-family: "Oswald", sans-serif; font-weight: 500; font-size: 21px;
    letter-spacing: 1.5px; line-height: 1; color: var(--gold);
  }
  .pouch--light .pouch__tagline { color: var(--tan); }

  .pouch__emblem {
    position: absolute; left: 50%; top: 344px; width: 44px; height: 44px;
    margin-left: -22px; transform: rotate(45deg); border-radius: 4px;
    background: linear-gradient(135deg, var(--gold-light), var(--gold-deep));
  }
  .pouch--light .pouch__emblem { background: var(--brown); }

  .pouch__badges { position: absolute; left: 54px; top: 562px; display: flex; gap: 10px; }
  .badge-age { width: 26px; height: 26px; border-radius: 50%; background: var(--white); border: 2px solid var(--warn-red); }
  .badge-warning { width: 0; height: 0; border-left: 13px solid transparent; border-right: 13px solid transparent; border-bottom: 23px solid var(--white); margin-top: 1px; }
  .pouch--light .badge-warning { border-bottom-color: #1a1a1a; }

  .pouch__rule { position: absolute; left: 0; top: 593px; width: 100%; height: 2px; background: var(--gold); }
  .pouch--light .pouch__rule { background: var(--tan); }

  .pouch__band {
    position: absolute; left: 0; top: 601px; width: 100%; height: 60px;
    background: linear-gradient(90deg, var(--gold-deep), var(--gold-light) 45%, var(--gold) 70%, var(--gold-deep));
  }
  .pouch--light .pouch__band { background: var(--brown-band); }

  .pouch__weight {
    position: absolute; left: 0; top: 629px; width: 100%; text-align: center;
    font-size: 11px; font-weight: 700; line-height: 1.3; color: #1a1a1a;
  }
  .pouch--light .pouch__weight { color: var(--white); }
</style>
</head>
<body>
  <section class="pouch pouch--dark">
    <svg class="pouch__art" viewBox="0 0 410 661" aria-hidden="true">
      <defs>
        <linearGradient id="leafDark" x1="0" y1="0" x2="0" y2="1">
          <stop offset="0" stop-color="#4f7238"/>
          <stop offset="1" stop-color="#7d9e5e"/>
        </linearGradient>
        <linearGradient id="beanDark" x1="0" y1="0" x2="0" y2="1">
          <stop offset="0" stop-color="#7a4d2e"/>
          <stop offset="1" stop-color="#3b2313"/>
        </linearGradient>
      </defs>
      <path role="img" aria-label="Cannabis leaves fanning down from the top edge" fill="url(#leafDark)" opacity=".85"
            d="M0 0 H410 V175 Q380 150 345 138 Q300 105 280 70 Q205 120 130 72 Q100 115 40 140 Q18 150 0 180 Z"/>
      <path role="img" aria-label="Photo of roasted coffee beans with cannabis leaves" fill="url(#beanDark)"
            d="M0 420 Q40 400 85 412 Q130 398 175 420 Q230 396 285 418 Q340 398 410 408 V601 H0 Z"/>
    </svg>
    <div class="pouch__mark"></div>
    <h1 class="pouch__name">Drifting Marlo’s</h1>
    <p class="pouch__tagline">COFFEE + CANNABIS</p>
    <div class="pouch__emblem" role="img" aria-label="Gold cannabis leaf emblem"></div>
    <div class="pouch__badges">
      <span class="badge-age"></span>
      <span class="badge-warning"></span>
    </div>
    <div class="pouch__rule"></div>
    <div class="pouch__band"></div>
    <p class="pouch__weight">Net WT 0.0353 OZ<br>(1.G)</p>
  </section>

  <section class="pouch pouch--light">
    <svg class="pouch__art" viewBox="0 0 410 661" aria-hidden="true">
      <defs>
        <linearGradient id="leafLight" x1="0" y1="0" x2="0" y2="1">
          <stop offset="0" stop-color="#9fb98a"/>
          <stop offset="1" stop-color="#7fa062"/>
        </linearGradient>
        <linearGradient id="beanLight" x1="0" y1="0" x2="0" y2="1">
          <stop offset="0" stop-color="#9a6a45"/>
          <stop offset="1" stop-color="#6e4a30"/>
        </linearGradient>
      </defs>
      <path role="img" aria-label="Cannabis leaves fanning down from the top edge" fill="url(#leafLight)" opacity=".8"
            d="M0 0 H410 V175 Q380 150 345 138 Q300 105 280 70 Q205 120 130 72 Q100 115 40 140 Q18 150 0 180 Z"/>
      <path role="img" aria-label="Photo of roasted coffee beans with cannabis leaves" fill="url(#beanLight)" opacity=".9"
            d="M0 420 Q40 400 85 412 Q130 398 175 420 Q230 396 285 418 Q340 398 410 408 V601 H0 Z"/>
    </svg>
    <div class="pouch__mark"></div>
    <h1 class="pouch__name">Drifting Marlo’s</h1>
    <p class="pouch__tagline">COFFEE + CANNABIS</p>
    <div class="pouch__emblem" role="img" aria-label="Brown cannabis leaf emblem"></div>
    <div class="pouch__badges">
      <span class="badge-age"></span>
      <span class="badge-warning"></span>
    </div>
    <div class="pouch__rule"></div>
    <div class="pouch__band"></div>
    <p class="pouch__weight">Net WT 0.0353 OZ<br>(1.G)</p>
  </section>
</body>
</html>
```